Website redesign

Looking to redesign our existing website. (quill7meadows.com.au)
New design needs to be bright, fun and have an easy flowing.
The website needs to be design with call to action.

Some examples of other websites:
fernquaylo.com
tovanmilk.com.au

We are happy with the content of our existing website.

Target Market(s)

other businesses

Industry/Entity Type

Business Service

Number of Pages Required

5+ page

Requirements
Must have
• Theme redesign
Cool animation similar to fernquaylo.com

```html
<!DOCTYPE html>
<html lang="en">
<head>
<meta charset="utf-8">
<title>Quill Meadows – Virtual Assistants</title>
<link href="https://fonts.googleapis.com/css2?family=Source+Sans+3:wght@300;400;600;700&display=swap" rel="stylesheet">
<style>
:root{
  --blue:#0ea5e0;
  --blue-dark:#1b93d1;
  --ink:#2c3440;
  --text:#555c66;
  --muted:#8a9099;
  --hero-bg:#f3f5f7;
  --soft-bg:#eef3fa;
  --white:#ffffff;
  --line:#cfd6de;
}
*{box-sizing:border-box;margin:0;padding:0}
html,body{width:1200px;height:3647px;overflow:hidden}
body{font-family:"Source Sans 3",Arial,sans-serif;color:var(--ink);background:var(--white);position:relative}
.abs{position:absolute}
section,header,footer{position:absolute;left:0;width:1200px}

/* header */
.site-header{top:0;height:110px;background:var(--white);box-shadow:0 2px 6px rgba(0,0,0,.08);z-index:2}
.brand{position:absolute;left:66px;top:38px;display:flex;align-items:center;gap:10px;font-size:22px;font-weight:600;color:var(--ink);letter-spacing:.5px}
.brand .dot{width:14px;height:14px;border-radius:50%;background:var(--blue)}
.nav a{position:absolute;top:44px;font-size:15px;color:var(--ink);text-decoration:none}
.nav .active::after{content:"";position:absolute;left:0;right:0;top:62px;height:3px;background:var(--blue)}

/* buttons */
.btn{position:absolute;display:flex;align-items:center;justify-content:center;font-size:13px;border-radius:2px}
.btn-solid{background:var(--blue);color:var(--white)}
.btn-ghost{border:2px solid var(--blue);color:var(--blue);background:var(--white)}

/* hero */
.hero{top:110px;height:748px;background:var(--hero-bg)}
.hero-title{position:absolute;left:40px;width:456px;top:74px;text-align:center;font-size:30px;line-height:48px;font-weight:400;color:var(--ink)}
.hero-title b{color:var(--blue);font-weight:700}
.hero-sub{position:absolute;left:40px;width:456px;top:184px;text-align:center;font-size:17px}
.video{position:absolute;left:617px;top:81px;width:443px;height:272px;border-radius:14px;border:3px solid var(--white);box-shadow:0 4px 14px rgba(0,0,0,.18);background:linear-gradient(120deg,#b9cbd4,#8cc7e6 50%,#aab3bb)}
.play{position:absolute;left:197px;top:112px;width:46px;height:46px;border-radius:50%;background:var(--white)}
.play::after{content:"";position:absolute;left:18px;top:13px;border-left:15px solid #8cc7e6;border-top:10px solid transparent;border-bottom:10px solid transparent}
.deco-arrow{position:absolute;width:54px;height:54px;border-radius:6px;background:#cfe6f4}
.intro-card{position:absolute;left:222px;top:443px;width:755px;height:253px;background:var(--white);box-shadow:0 2px 10px rgba(0,0,0,.08);text-align:center}
.intro-card h2{font-size:14px;font-weight:700;margin-top:34px}
.intro-card p{font-size:11px;line-height:24px;color:var(--text);width:530px;margin:26px auto 0}

/* process */
.process{top:858px;height:1192px;background:var(--soft-bg)}
.section-title{position:absolute;left:0;width:1200px;text-align:center;font-size:26px;font-weight:300;color:var(--ink);letter-spacing:.5px}
.section-title b{font-weight:700}
.step{position:absolute;width:330px}
.step .num{position:absolute;left:-70px;top:-18px;width:44px;height:44px;border-radius:50%;background:var(--blue);color:var(--white);font-size:18px;display:flex;align-items:center;justify-content:center}
.step h3{font-size:15px;font-weight:700;line-height:22px;color:var(--ink)}
.step p{font-size:15.5px;line-height:24px;font-weight:300;color:var(--muted)}
.photo{position:absolute}

/* services */
.services{top:2050px;height:642px;background:var(--white)}
.services .lead{position:absolute;left:0;width:1200px;top:110px;text-align:center;font-size:11px;color:var(--ink)}
.services .glad{position:absolute;left:0;width:1196px;top:133px;text-align:center;font-size:13px;font-weight:700;color:var(--blue)}
.card{position:absolute;top:234px;width:215px;height:240px;background:var(--white);box-shadow:0 2px 8px rgba(0,0,0,.12);text-align:center}
.card .icon{position:absolute;left:78px;top:82px;width:60px;height:76px;border-radius:30px;background:var(--blue)}
.card h4{margin-top:98px;font-size:13px;line-height:24px;color:var(--blue);font-weight:700}
.card small{font-size:10px;color:var(--ink)}
.simple{position:absolute;left:0;width:1200px;top:544px;text-align:center;font-size:20px;font-weight:300;line-height:24px;color:var(--text)}
.simple b{color:var(--blue);font-weight:700}

/* quote */
.quote{top:2692px;height:758px;background:var(--soft-bg)}
.quote .sub{position:absolute;left:0;width:1200px;top:114px;text-align:center;font-size:16px;font-weight:300;color:var(--muted)}
.why h3{position:absolute;left:100px;width:396px;top:206px;text-align:center;font-size:28px;font-weight:600;color:var(--ink)}
.why h3 b{color:var(--blue)}
.why p{position:absolute;left:100px;width:396px;top:269px;text-align:center;font-size:16px}
.perks{position:absolute;left:154px;top:338px;list-style:none}
.perks li{display:flex;align-items:center;gap:16px;height:48px;font-size:15px;letter-spacing:.3px}
.field{position:absolute;background:var(--white);border:1px solid var(--line);font-size:12px;color:var(--muted);padding:0 11px;display:flex;align-items:center}
.field.area{align-items:flex-start;padding-top:10px}
.captcha{position:absolute;left:812px;top:556px;width:178px;height:43px;background:#222;color:var(--white);font-size:8px;display:flex;align-items:center;padding-left:8px;gap:8px}
.captcha span.box{width:16px;height:16px;background:var(--white);border-radius:2px}
.newsletter{position:absolute;left:800px;top:627px;font-size:12px;display:flex;align-items:center;gap:14px}
.newsletter i{width:9px;height:9px;border:2px solid var(--ink);border-radius:50%}

/* footer */
.site-footer{top:3450px;height:197px;background:var(--blue);color:var(--white);text-align:center}
.site-footer .name{position:absolute;left:0;width:1200px;top:52px;font-size:24px;font-weight:600;letter-spacing:.5px}
.site-footer .tag{position:absolute;left:0;width:1200px;top:134px;font-size:12px}
.site-footer .copy{position:absolute;left:0;width:1200px;top:168px;font-size:9px}
</style>
</head>
<body>

<header class="site-header">
  <div class="brand"><span class="dot"></span>QUILL MEADOWS</div>
  <nav class="nav">
    <a class="active" href="#" style="left:627px">Home</a>
    <a href="#" style="left:722px">Our Story</a>
    <a href="#" style="left:841px">Tips &amp; Tricks</a>
    <a href="#" style="left:979px">Contact Us</a>
    <a href="#" style="left:1107px">FAQ</a>
  </nav>
</header>

<section class="hero">
  <h1 class="hero-title">VIRTUAL ASSISTANT? <b>MORE<br>LIKE VALUABLE ASSET!</b></h1>
  <p class="hero-sub">Tech nerds on standby for setup, support and comms!</p>
  <a class="btn btn-solid" style="left:75px;top:249px;width:181px;height:44px">Call Now</a>
  <a class="btn btn-ghost" style="left:280px;top:249px;width:181px;height:44px">Get a Quote</a>
  <div class="deco-arrow" role="img" aria-label="Hand-drawn arrow pointing to the video" style="left:534px;top:30px"></div>
  <div class="deco-arrow" role="img" aria-label="Hand-drawn arrow pointing to the video" style="left:1100px;top:330px"></div>
  <div class="video" role="img" aria-label="Video thumbnail of a team meeting"><span class="play"></span></div>
  <div class="intro-card">
    <h2>Outsourcing. A big word that means big things for your business.</h2>
    <p>Virtual Assistants are the superheroes of the modern office. They can do everything your team can do on a computer at a fraction of the price! (Well, maybe not high five you when you've had a win, but a virtual high five is definitely on the table!)</p>
    <a class="btn btn-ghost" style="left:288px;top:178px;width:180px;height:44px">Get a Quote</a>
  </div>
</section>

<section class="process">
  <h2 class="section-title" style="top:32px">THE PROCESS</h2>
  <div class="step" style="left:274px;top:115px"><span class="num">1</span>
    <h3>Provide Your Preferred Qualifications.</h3>
    <p>Set up a call with our team to specify the requirements and qualifications you're searching for in a Virtual Assistant. This will be our checklist for your perfect assistant! From there, we'll take care of shortlisting, testing, background checking and recruiting.</p></div>
  <div class="step" style="left:274px;top:307px"><span class="num">2</span>
    <h3>Endorsing the Shortlisted Candidates</h3>
    <p>After the thorough vetting process, we'll put forward the best candidate. You can then conduct the final interview on your preferred communication platform at a time that suits you. Once the schedule is set, we'll let the candidates know!</p></div>
  <div class="step" style="left:274px;top:523px"><span class="num">3</span>
    <h3>Conducting the Final Interview</h3>
    <p>The final interview is the perfect time to get to know the candidates. It'll help to have a list of questions prepared that will help you pick out the chosen one!</p></div>
  <div class="photo" role="img" aria-label="Photo of a man on the phone at his laptop" style="left:712px;top:161px;width:488px;height:363px;background:linear-gradient(120deg,#5e8e98,#a9c2c3 55%,#7fa0a4)"></div>
  <div class="step" style="left:711px;top:692px;width:330px"><span class="num">4</span>
    <h3>Setting up the Tools</h3>
    <p>Once you've chosen your Virtual Assistant, it's time for their system to be set up. You can get your own IT team onto the installation, otherwise, we've got a super team of tech peeps who can do it for you.</p></div>
  <div class="step" style="left:711px;top:860px;width:330px"><span class="num">5</span>
    <h3>Your Magical Journey Begins</h3>
    <p>Now you and your Virtual Assistant are all set up and ready to rumble! Feel the magic of having a reliable assistant to take on all the menial, repetitive, time-consuming tasks, and focus your energy on more important things. Meet new clients, explore business opportunities, or just spend some time with friends and family!</p></div>
  <a class="btn btn-ghost" style="left:749px;top:1096px;width:181px;height:44px">Get a Quote</a>
  <div class="photo" role="img" aria-label="Photo of a smiling man in a navy dotted shirt" style="left:176px;top:815px;width:402px;height:377px;border-radius:160px 160px 0 0;background:linear-gradient(180deg,#d9b8a0 0%,#c9a48c 45%,#1f2a44 60%,#1a2440)"></div>
</section>

<section class="services">
  <h2 class="section-title" style="top:48px">OUR <b>SERVICES</b></h2>
  <p class="lead">We'll help you save tens (or even hundreds!) of thousands of dollars per year. But what do WE actually do?</p>
  <p class="glad">GLAD YOU ASKED!</p>
  <div class="card" style="left:66px"><span class="icon" role="img" aria-label="Icon of a person with glasses"></span></div>
  <div class="card" style="left:351px"><span class="icon" role="img" aria-label="Headset support icon"></span></div>
  <div class="card" style="left:635px">
    <svg class="abs" style="left:91px;top:38px" width="34" height="34" viewBox="0 0 34 34" fill="none" stroke="#2c3440" stroke-width="2"><rect x="2" y="2" width="30" height="30"/><rect x="7" y="7" width="8" height="20"/><path d="M19 8h9M19 13h3M24 13h4M19 18h3M24 18h4M19 23h3M24 23h4"/></svg>
    <h4>SET UP THE PHONE<br>SYSTEM</h4><small>(Their Own Bat Phone!)</small></div>
  <div class="card" style="left:919px"><span class="icon" role="img" aria-label="Trophy icon" style="border-radius:6px"></span></div>
  <p class="simple">See? <b>It's that simple!</b> The only thing to do now is to finally<br>get started on the quote... just scroll down a little more.</p>
  <div class="abs" role="img" aria-label="Hand-drawn arrow pointing down" style="left:845px;top:598px;width:65px;height:107px;background:#5cc0ea;border-radius:8px;z-index:1"></div>
</section>

<section class="quote">
  <h2 class="section-title" style="top:56px">GET A <b>QUOTE</b></h2>
  <p class="sub">Fill in the form below to get a Quote for your own personal Virtual Assistant</p>
  <div class="why">
    <h3>MEET YOUR <b>NEW ASSISTANT</b></h3>
    <p>Why are we your new best outsourcing friend?</p>
  </div>
  <ul class="perks">
    <li><svg width="28" height="28" viewBox="0 0 28 28" fill="none" stroke="#0ea5e0" stroke-width="2.2"><circle cx="14" cy="14" r="12"/><path d="M8 14l4 4 8-8"/></svg>Your Own Virtual Assistant</li>
    <li><svg width="28" height="28" viewBox="0 0 28 28" fill="none" stroke="#0ea5e0" stroke-width="2.2"><circle cx="14" cy="14" r="12"/><path d="M8 14l4 4 8-8"/></svg>One Invoice Per Month</li>
    <li><svg width="28" height="28" viewBox="0 0 28 28" fill="none" stroke="#0ea5e0" stroke-width="2.2"><circle cx="14" cy="14" r="12"/><path d="M8 14l4 4 8-8"/></svg>No Super or TAX</li>
    <li><svg width="28" height="28" viewBox="0 0 28 28" fill="none" stroke="#0ea5e0" stroke-width="2.2"><circle cx="14" cy="14" r="12"/><path d="M8 14l4 4 8-8"/></svg>Dedicated To Your Business Only</li>
    <li><svg width="28" height="28" viewBox="0 0 28 28" fill="none" stroke="#0ea5e0" stroke-width="2.2"><circle cx="14" cy="14" r="12"/><path d="M8 14l4 4 8-8"/></svg>Dedicated Phone System</li>
    <li><svg width="28" height="28" viewBox="0 0 28 28" fill="none" stroke="#0ea5e0" stroke-width="2.2"><circle cx="14" cy="14" r="12"/><path d="M8 14l4 4 8-8"/></svg>IT Setup and Support</li>
  </ul>
  <div class="field" style="left:654px;top:228px;width:225px;height:33px">Your First Name</div>
  <div class="field" style="left:907px;top:228px;width:226px;height:33px">Your Surname</div>
  <div class="field" style="left:654px;top:283px;width:479px;height:33px">Business Name</div>
  <div class="field" style="left:654px;top:339px;width:225px;height:33px">Contact Number</div>
  <div class="field" style="left:907px;top:339px;width:226px;height:33px">Email</div>
  <div class="field area" style="left:654px;top:405px;width:479px;height:118px">Describe the tasks you'll need from your Virtual Assistant</div>
  <div class="captcha"><span class="box"></span>I'm not a robot</div>
  <div class="newsletter"><i></i>Subscribe to our newsletter</div>
  <a class="btn btn-solid" style="left:846px;top:679px;width:94px;height:32px">Submit</a>
  <div class="abs" role="img" aria-label="Illustration of a city skyline" style="left:520px;top:721px;width:164px;height:37px;background:#4fb9e6"></div>
</section>

<footer class="site-footer">
  <div class="name">QUILL MEADOWS</div>
  <p class="tag">Virtual Assistant? More Like Valuable Asset!</p>
  <p class="copy">© 2020 QUILL MEADOWS | All rights reserved.</p>
</footer>

</body>
</html>
```